Quorvex clinic business card - double sided for young clinic

I require business cards for my aesthetic clinic specialising in the below treatments. I would like the cards to be modern as my clinic base are young 22-35 years old. I require my logo on it and would like the edges to be rounded.

I have an aesthetic clinic specialising in :
Quorvex
Lip Enhancement
Chemical Peels
Facial Fillers
Non Surgical Face Lift

I would the cards to have the following information on them:
My logo - (in grey/silver)
address
Phone number
services

Colours :
White/grey/silver and red

a nice image on there, perhaps a set of lips as this is a main service i deliver

Company Name: PDA Address: 52 Farrowmere Road, 4 Brackwell High Street, KT9 4WQ Phone: 0208 794 2160 Website: www.penningtondoweaesthetics.co.uk

Target Market(s)

clinics 22-45 years old mainly female

Industry/Entity Type

Business

Contact Information for Business Card

as above

Requirements
Must have
• logo
• Address
• Email
• Phone number
• Services i offer
Nice to have
• images

```html
<!DOCTYPE html>
<html lang="en">
<head>
<meta charset="utf-8">
<title>PDA Aesthetics – Business Card</title>
<link rel="stylesheet" href="https://fonts.googleapis.com/css2?family=Tenor+Sans&display=swap">
<style>
  :root {
    --canvas: #ececec;
    --card: #ffffff;
    --red: #d94a52;
    --red-deep: #c63a43;
    --ink: #2b2b2b;
    --silver: #a7a7a7;
    --lip-light: #f06a86;
    --lip-dark: #c2183f;
  }
  * { box-sizing: border-box; margin: 0; padding: 0; }
  html, body {
    width: 1200px; height: 1000px; overflow: hidden;
    background: var(--canvas);
    font-family: "Tenor Sans", "Helvetica Neue", sans-serif;
  }
  .stage {
    position: relative; width: 1200px; height: 1000px;
    display: flex; align-items: center; justify-content: center; gap: 60px;
  }
  .card {
    position: relative; width: 500px; height: 290px;
    background: var(--card); border-radius: 16px; overflow: hidden;
    box-shadow: 0 10px 30px rgba(0,0,0,0.10);
  }

  /* Info side */
  .card-info__columns {
    position: absolute; top: 48px; left: 0; right: 0;
    display: flex; justify-content: center;
  }
  .services, .address { width: 200px; font-size: 12px; line-height: 1.6; color: var(--ink); letter-spacing: 0.04em; }
  .services { text-align: right; padding-right: 16px; border-right: 1.5px solid var(--red); }
  .address { padding-left: 16px; padding-top: 34px; }
  .heading { color: var(--red); font-size: 12px; letter-spacing: 0.06em; }
  .contact-band {
    position: absolute; left: 0; right: 0; top: 198px; height: 44px;
    background: linear-gradient(90deg, var(--red), var(--red-deep));
    display: flex; align-items: center; justify-content: space-around;
    color: #fff; font-size: 12px; letter-spacing: 0.04em; padding: 0 18px;
  }
  .contact-item { display: flex; align-items: center; gap: 7px; }
  .contact-item svg { width: 14px; height: 14px; fill: none; stroke: #fff; stroke-width: 1.4; }

  /* Brand side */
  .brand {
    position: absolute; top: 46px; left: 0; right: 0;
    display: flex; flex-direction: column; align-items: center; gap: 10px;
  }
  .brand__dot { width: 58px; height: 58px; border-radius: 50%; background: var(--silver); }
  .brand__name {
    color: var(--silver); font-size: 14px; letter-spacing: 0.18em; text-align: center; line-height: 1.35;
  }
  .brand__name .line-large { display: block; font-size: 24px; letter-spacing: 0.12em; }
  .lips-art {
    position: absolute; left: 160px; top: 190px; width: 180px; height: 62px;
    border-radius: 50% / 50%;
    background: radial-gradient(ellipse at 50% 40%, var(--lip-light), var(--lip-dark));
  }
</style>
</head>
<body>
<main class="stage">
  <section class="card card-info" aria-label="Card reverse: services and contact">
    <div class="card-info__columns">
      <div class="services">
        <p class="heading">SPECIALISING IN</p>
        <p>QUORVEX | LIP ENHANCEMENT</p>
        <p>CHEMICAL PEELS | FACIAL FILLERS</p>
        <p>NON SURGICAL FACE LIFT</p>
      </div>
      <div class="address">
        <p class="heading">ADDRESS</p>
        <p>NO.-X | YOUR STREET NAME</p>
        <p>YOUR PLACE | STATE</p>
      </div>
    </div>
    <div class="contact-band">
      <span class="contact-item">
        <svg viewBox="0 0 16 16"><rect x="1.5" y="3.5" width="13" height="9"/><path d="M1.5 3.5 8 9l6.5-5.5"/></svg>
        YOUREMAILID@EMAIL.COM
      </span>
      <span class="contact-item">
        <svg viewBox="0 0 16 16"><path d="M4 2h2.5l1 3-1.5 1a8 8 0 0 0 4 4l1-1.5 3 1V12a2 2 0 0 1-2 2A10 10 0 0 1 2 4a2 2 0 0 1 2-2z"/></svg>
        123 456 7890
      </span>
      <span class="contact-item">
        <svg viewBox="0 0 16 16"><circle cx="8" cy="8" r="6.5"/><ellipse cx="8" cy="8" rx="3" ry="6.5"/><path d="M1.5 8h13"/></svg>
        YOURWEB.COM
      </span>
    </div>
  </section>

  <section class="card card-brand" aria-label="Card front: brand">
    <div class="brand">
      <span class="brand__dot"></span>
      <p class="brand__name">PENNINGTON DOWE<span class="line-large">AESTHETICS</span></p>
    </div>
    <div class="lips-art" role="img" aria-label="Illustration of glossy red lips"></div>
  </section>
</main>
</body>
</html>
```